Website Design Request - Management Consulting Firm

We need a Website designed for an IT Management Staffing and Recruiting firm called VANTREX based in San Francisco.

The firm is an high-end technology staffing agency. Our focus is on quality and high-caliber candidates rather than quantity.

The website will have two main home pages. One for the recruiter and another on for the candidates.

The website needs to optimize for mobile devices as well.

I have attached few mock-ups that I have done just to show what I am thinking. The UI needs to be very clean, fluid, and it needs to have a modern, rustic, professional feel to it.

Target Market(s)

Technology Manager, Director, VP, CIO of Companies that have $4b-10b dollar revenue. Such as hollowmeadowgoods.example , https://www.quillbarrow.example/, lumatic.example, zib.example

Industry/Entity Type

Management Consulting

Number of Pages Required

5+ page

Font styles to use
Sans Serif

Colors
f37122
ffffff

Requirements
Must have
• Please review mock-ups for suggestions
Nice to have
Should not have

```html
<!DOCTYPE html>
<html lang="en">
<head>
<meta charset="utf-8">
<title>VANTREX – Project Management Consulting</title>
<link rel="stylesheet" href="https://fonts.googleapis.com/css2?family=Jost:wght@400;500;600&display=swap">
<style>
:root{
  --orange:#f37122;
  --white:#ffffff;
  --ink:#222222;
  --text:#444444;
  --muted:#777777;
  --topbar:#2b2b2b;
  --band:#f1f1f1;
  --tab:#efefef;
  --news:#333333;
  --footer:#121212;
}
*{box-sizing:border-box;margin:0;padding:0}
html,body{width:1200px;height:2182px;overflow:hidden}
body{position:relative;font-family:"Jost",sans-serif;color:var(--text);background:var(--white)}
.abs{position:absolute}
a{color:inherit;text-decoration:none}

/* top bar */
.topbar{left:0;top:0;width:1200px;height:34px;background:var(--topbar);color:var(--white);font-size:14px}
.topbar .link{top:8px}
.topbar .sep{left:826px;top:9px;width:1px;height:16px;background:#777}
.auth{top:4px;height:26px;background:var(--orange);color:var(--white);font-size:14px;display:flex;align-items:center;gap:5px;padding:0 8px}

/* header */
.header{left:0;top:34px;width:1200px;height:87px;background:var(--white)}
.brand{left:99px;top:10px}
.brand-name{font-size:48px;font-weight:500;color:var(--orange);letter-spacing:3px;line-height:1}
.brand-sub{font-size:13px;color:#333;letter-spacing:1px;margin-top:4px}
.nav a{position:absolute;top:34px;font-size:14px;color:#333}
.nav a.active{color:var(--orange)}

/* hero */
.hero{left:0;top:121px;width:1200px;height:599px;background:radial-gradient(ellipse at 75% 45%,#3a6fa8 0%,#1c3556 25%,#0b1422 55%,#050608 100%)}
.hero h1{left:0;width:1200px;top:194px;text-align:center;font-size:32px;font-weight:500;color:var(--white)}
.hero .lead{left:0;width:1200px;top:244px;text-align:center;font-size:16px;color:var(--white)}
.email-field{left:159px;top:308px;width:744px;height:41px;background:var(--white);font-size:14px;color:#888;padding:11px 15px}
.btn-start{left:913px;top:308px;width:127px;height:41px;background:var(--orange);color:var(--white);font-size:16px;text-align:center;line-height:41px}
.terms{left:0;width:1200px;top:390px;text-align:center;font-size:15px;color:var(--white)}
.terms u{color:#cfcfcf}
.btn-upload{left:390px;top:423px;width:135px;height:35px;background:#3b3b3b;color:var(--white);font-size:15px;text-align:center;line-height:35px}
.upload-note{left:545px;top:430px;font-size:15px;color:var(--white)}

/* tabs */
.tabs{left:99px;top:764px;width:1002px;height:75px;background:var(--tab)}
.tab{position:absolute;top:0;height:75px;display:flex;align-items:center;justify-content:center;gap:14px;font-size:26px;color:#333}
.tab.active{background:var(--orange);color:var(--white)}
.tab.active::after{content:"";position:absolute;bottom:-9px;left:50%;margin-left:-9px;border:9px solid transparent;border-bottom:0;border-top-color:var(--orange)}
.tab-sep{position:absolute;left:639px;top:14px;width:1px;height:47px;background:#d6d6d6}

/* focus cards */
.card{top:890px;width:317px}
.card .photo{height:247px;border:4px solid #333;background:linear-gradient(160deg,#e9eef3,#b7c3cf 60%,#8e9aa6);position:relative}
.card .badge{position:absolute;left:50%;bottom:-4px;margin-left:-52px;width:104px;height:52px;background:#333;border-radius:52px 52px 0 0;display:flex;justify-content:center;padding-top:10px}
.card h3{text-align:center;font-size:21px;font-weight:500;color:var(--ink);margin-top:20px}
.card p{text-align:center;font-size:13.5px;line-height:22px;color:#444;margin-top:8px;padding:0 4px}

/* hiring */
.hiring{left:0;top:1321px;width:1200px;height:509px;background:var(--band)}
.hiring h2{left:0;width:1200px;top:20px;text-align:center;font-size:32px;font-weight:500;color:var(--ink)}
.hiring h2 span{color:var(--orange)}
.rule{top:88px;height:1px;background:#cfcfcf;width:190px}
.rule-dot{left:592px;top:80px;width:16px;height:16px;border-radius:50%;background:#bbb}
.hiring .sub{left:0;width:1200px;top:122px;text-align:center;font-size:20px;color:var(--ink)}
.col h4{font-size:21px;font-weight:500;color:#333}
.col .bar{width:55px;height:2px;background:#aaa;margin-top:8px}
.item{position:absolute;display:flex;gap:12px;font-size:15.5px;line-height:22px;color:#333}
.item svg{flex:none;margin-top:3px}
.btn-sm{position:absolute;height:32px;background:var(--orange);color:var(--white);font-size:14px;line-height:32px;padding:0 11px}
.col-divider{left:589px;top:199px;width:1px;height:269px;background:#d4d4d4}

/* newsletter */
.newsletter{left:0;top:1830px;width:1200px;height:73px;background:var(--news);color:var(--white)}
.nl-icon{left:106px;top:17px;width:40px;height:40px;border-radius:50%;background:var(--orange);border:3px solid var(--white);display:flex;align-items:center;justify-content:center}
.nl-title{left:164px;top:17px;font-size:26px;font-weight:500}
.nl-text{left:349px;top:28px;font-size:14px;color:#ddd}
.nl-field{left:663px;top:18px;width:326px;height:37px;background:var(--white);color:#888;font-size:14px;padding:9px 16px}
.nl-btn{left:989px;top:18px;width:103px;height:37px;background:var(--orange);font-size:16px;font-weight:500;text-align:center;line-height:37px}

/* footer */
.footer{left:0;top:1903px;width:1200px;height:235px;background:var(--footer);color:#ddd}
.footer h5{position:absolute;font-size:20px;font-weight:500;color:var(--white)}
.f-brand{left:99px;top:58px}
.f-brand .brand-name{color:#9a9a9a;font-size:40px}
.f-brand .brand-sub{color:#9a9a9a;font-size:11px}
.f-about{left:99px;top:134px;width:250px;font-size:13px;line-height:23px;color:#ddd}
.f-links{left:400px;top:58px;list-style:none;font-size:14px;line-height:29px}
.f-links li::before{content:"•";margin-right:8px}
.f-address{left:566px;top:58px;font-size:13px;line-height:22px}
.f-row{display:flex;gap:10px;align-items:flex-start}
.map{left:884px;top:81px;width:217px;height:128px;background:linear-gradient(135deg,#e7e4dc,#d9d6cc)}

/* copyright */
.copy{left:0;top:2138px;width:1200px;height:44px;background:var(--orange);color:var(--white);font-size:14px}
.copy p{position:absolute;left:99px;top:13px}
.social{position:absolute;top:8px;width:28px;height:28px;border:2px solid var(--white);border-radius:50%}
</style>
</head>
<body>

<!-- Top bar -->
<div class="abs topbar">
  <a class="abs link" href="#" style="left:726px">Professionals</a>
  <span class="abs sep"></span>
  <a class="abs link" href="#" style="left:847px">Employers</a>
  <a class="abs auth" href="#" style="left:935px">
    <svg width="12" height="14" viewBox="0 0 12 14"><rect x="1" y="6" width="10" height="8" fill="#fff"/><path d="M3 6V4a3 3 0 0 1 6 0v2" stroke="#fff" stroke-width="1.6" fill="none"/></svg>Sign In</a>
  <a class="abs auth" href="#" style="left:1016px">
    <svg width="14" height="14" viewBox="0 0 14 14"><rect x="1" y="2" width="10" height="11" stroke="#fff" stroke-width="1.4" fill="none"/><path d="M5 9l7-7" stroke="#fff" stroke-width="1.6"/></svg>Sign Up</a>
</div>

<!-- Header -->
<header class="abs header">
  <div class="abs brand">
    <div class="brand-name">VANTREX</div>
    <div class="brand-sub">PROJECT MANAGEMENT CONSULTING</div>
  </div>
  <nav class="nav">
    <a class="active" href="#" style="left:571px">Home</a>
    <a href="#" style="left:673px">About Us</a>
    <a href="#" style="left:797px">Services</a>
    <a href="#" style="left:914px">Clients</a>
    <a href="#" style="left:1023px">Job Seekers</a>
  </nav>
</header>

<!-- Hero -->
<section class="abs hero" role="img" aria-label="Photo of a hand holding a tablet with a glowing globe and network icons on a dark background">
  <h1 class="abs">Hire Top IT Project Management Talents</h1>
  <p class="abs lead">Search Our network, Shortlist Candidates, Send Interview Requests &amp; Fill Positions Fast</p>
  <div class="abs email-field">Your Business Email Address</div>
  <a class="abs btn-start" href="#">Get Started</a>
  <p class="abs terms">By entering your email address, you agree to our <u>Terms &amp; Conditions</u>. Looking for a job?</p>
  <a class="abs btn-upload" href="#">Upload Resume</a>
  <p class="abs upload-note">and let companies dend you offers.</p>
</section>

<!-- Tabs -->
<div class="abs tabs">
  <div class="tab active" style="left:0;width:300px">
    <svg width="34" height="34" viewBox="0 0 34 34"><circle cx="14" cy="14" r="10" stroke="#fff" stroke-width="3" fill="none"/><path d="M21 21l9 9" stroke="#fff" stroke-width="4" stroke-linecap="round"/><circle cx="14" cy="12" r="3" fill="#fff"/><path d="M8 19a6 5 0 0 1 12 0z" fill="#fff"/></svg>
    Our Focus</div>
  <div class="tab" style="left:300px;width:339px">
    <svg width="32" height="34" viewBox="0 0 32 34"><circle cx="13" cy="9" r="7" fill="#333"/><path d="M1 33c0-9 5-15 12-15 4 0 6 2 7 3l-4 12z" fill="#333"/><path d="M17 26l4 4 9-10" stroke="#333" stroke-width="3" fill="none"/></svg>
    Why Us</div>
  <span class="tab-sep"></span>
  <div class="tab" style="left:640px;width:362px">
    <svg width="34" height="34" viewBox="0 0 34 34"><circle cx="17" cy="17" r="10" stroke="#333" stroke-width="4" fill="none" stroke-dasharray="5 3"/><circle cx="17" cy="17" r="5" stroke="#333" stroke-width="2.5" fill="none"/></svg>
    How It Works?</div>
</div>

<!-- Focus cards -->
<article class="abs card" style="left:99px">
  <div class="photo" role="img" aria-label="Photo of a presenter at a whiteboard leading a team meeting">
    <div class="badge"><svg width="28" height="32" viewBox="0 0 28 32"><circle cx="14" cy="8" r="7" fill="#fff"/><path d="M0 32c0-10 6-15 14-15s14 5 14 15z" fill="#fff"/></svg></div>
  </div>
  <h3>Project Managers</h3>
  <p>Manage IT Projects, Programs and Portfolio from start to finish. Get your projects back on track with our highly vetted consultants. Conduct Project audits, lessons learned and post-mortem.</p>
</article>

<article class="abs card" style="left:441px">
  <div class="photo" role="img" aria-label="Photo of a speaker addressing a seated audience">
    <div class="badge"><svg width="34" height="32" viewBox="0 0 34 32"><circle cx="17" cy="16" r="15" stroke="#fff" stroke-width="2" fill="none"/><circle cx="11" cy="12" r="3" fill="#fff"/><circle cx="23" cy="12" r="3" fill="#fff"/><circle cx="17" cy="10" r="3" fill="#fff"/><rect x="8" y="16" width="18" height="8" rx="2" fill="#fff"/></svg></div>
  </div>
  <h3>PMO Leadership</h3>
  <p>Stand up PMO office and project governance. Re-vamp or optimize existing IT Project Management Processes. Temporarily run IT PMO through our highly qualified PM Leaders</p>
</article>

<article class="abs card" style="left:784px">
  <div class="photo" role="img" aria-label="Photo of three colleagues reviewing work at a computer">
    <div class="badge"><svg width="32" height="32" viewBox="0 0 32 32"><circle cx="8" cy="6" r="5" fill="#fff"/><path d="M2 32V15h12v17z" fill="#fff"/><rect x="16" y="2" width="14" height="12" stroke="#fff" stroke-width="2" fill="none"/><path d="M14 16l6-4" stroke="#fff" stroke-width="2"/></svg></div>
  </div>
  <h3>PM Trainer &amp; Coaches</h3>
  <p>Individual coaching or group project management training. Setup Project Portfolio Management Tools. Drive Project Management Governance and adoption.</p>
</article>

<!-- Hiring flexibility -->
<section class="abs hiring">
  <h2 class="abs">Hiring <span>Flexiblity</span></h2>
  <span class="abs rule" style="left:394px"></span>
  <span class="abs rule-dot"></span>
  <span class="abs rule" style="left:616px"></span>
  <p class="abs sub">Hire on hourly or bring them on as permanent employees</p>

  <div class="abs col" style="left:99px;top:196px">
    <h4>Contract Roles</h4><div class="bar"></div>
  </div>
  <div class="item" style="left:99px;top:260px;width:440px">
    <svg width="17" height="17" viewBox="0 0 17 17"><circle cx="8.5" cy="8.5" r="7" stroke="#222" stroke-width="2" fill="none"/><path d="M8.5 4.5v4h3" stroke="#222" stroke-width="2" fill="none"/></svg>
    <span>Flexible hourly rate. Ideal for contract, part-time, or interim positions. Structure as needed.</span></div>
  <div class="item" style="left:99px;top:330px">
    <svg width="17" height="19" viewBox="0 0 17 19"><ellipse cx="8.5" cy="3.5" rx="8" ry="3" fill="#222"/><path d="M.5 6c0 4 16 4 16 0v4c0 4-16 4-16 0zM.5 12c0 4 16 4 16 0v3c0 4-16 4-16 0z" fill="#222"/></svg>
    <span>Search our database and schedule interviews directly.</span></div>
  <div class="item" style="left:99px;top:385px">
    <svg width="20" height="19" viewBox="0 0 20 19"><path d="M0 0h20l-8 9v10l-4-3V9z" fill="#222"/></svg>
    <span>25% Cheaper than traditional staffing firms.</span></div>
  <a class="btn-sm" href="#" style="left:99px;top:433px">Search Our Network</a>

  <span class="abs col-divider"></span>

  <div class="abs col" style="left:631px;top:196px">
    <h4>Permanent Roles</h4><div class="bar"></div>
  </div>
  <div class="item" style="left:631px;top:260px">
    <svg width="19" height="19" viewBox="0 0 19 19"><circle cx="9.5" cy="9.5" r="8.5" stroke="#222" stroke-width="1.6" fill="none"/><path d="M4 5c3 1 4 4 2 6l-2 1M11 3c2 2 4 3 6 3M12 12c2 0 3 2 3 4" stroke="#222" stroke-width="2.4" fill="none"/></svg>
    <span>National Reach - find the best candidate in the nation.</span></div>
  <div class="item" style="left:631px;top:322px">
    <svg width="19" height="19" viewBox="0 0 19 19"><circle cx="9.5" cy="9.5" r="8.5" stroke="#222" stroke-width="1.4" fill="none"/><text x="9.5" y="14" font-size="12" text-anchor="middle" fill="#222" font-family="Jost,sans-serif">$</text></svg>
    <span>50% Cheaperr than traditional recruiting fees.</span></div>
  <div class="item" style="left:631px;top:385px">
    <svg width="19" height="19" viewBox="0 0 19 19"><rect x="0" y="8" width="4" height="11" fill="#222"/><path d="M6 8l4-8c2 0 3 2 2 5h6c1 0 1 2 0 2 1 1 1 2 0 3 1 1 0 2-1 3 0 2-1 3-2 3H6z" fill="#222"/></svg>
    <span>White Glove Services for all permanent roles</span></div>
  <a class="btn-sm" href="#" style="left:631px;top:433px">Contact Us</a>
</section>

<!-- Newsletter -->
<section class="abs newsletter">
  <div class="abs nl-icon"><svg width="20" height="14" viewBox="0 0 20 14"><rect width="20" height="14" rx="2" fill="#fff"/><path d="M1 1l9 7 9-7" stroke="#f37122" stroke-width="1.6" fill="none"/></svg></div>
  <div class="abs nl-title">News Letter</div>
  <p class="abs nl-text">Enter your email adrress for getting updates</p>
  <div class="abs nl-field">Email</div>
  <a class="abs nl-btn" href="#">Subscribe</a>
</section>

<!-- Footer -->
<footer class="abs footer">
  <div class="abs f-brand">
    <div class="brand-name">VANTREX</div>
    <div class="brand-sub">PROJECT MANAGEMENT CONSULTING</div>
  </div>
  <p class="abs f-about">Duis aute irure dolor in reprehenderit in voluptate velit esse cillum dolore eu fugiat nulla pariatur. Excepteur sint occaecat</p>

  <h5 style="left:394px;top:37px">Quick links</h5>
  <ul class="abs f-links">
    <li>Home</li><li>About Us</li><li>Services</li><li>Clients</li><li>Job Seekers</li>
  </ul>

  <h5 style="left:566px;top:37px">Address</h5>
  <div class="abs f-address">
    <div class="f-row" style="width:270px">
      <svg width="11" height="15" viewBox="0 0 11 15" style="margin-top:4px;flex:none"><path d="M5.5 15C2 10 0 7.5 0 5.5a5.5 5.5 0 0 1 11 0C11 7.5 9 10 5.5 15z" fill="#f37122"/><circle cx="5.5" cy="5.5" r="2" fill="#121212"/></svg>
      <div><span style="color:#fff">Vantrex Project Management Consulting</span><br>337, Lorem ipsum dolor sit amet,<br>consectetur adipiscing elit, sed do</div>
    </div>
    <div class="f-row" style="margin-top:10px">
      <svg width="12" height="12" viewBox="0 0 12 12" style="margin-top:5px"><path d="M2 0l3 3-2 2c1 2 2 3 4 4l2-2 3 3-2 2C5 12 0 7 0 2z" fill="#f37122"/></svg>
      <span style="color:#fff">123-456-7890</span></div>
    <div class="f-row" style="margin-top:10px">
      <svg width="12" height="9" viewBox="0 0 12 9" style="margin-top:7px"><rect width="12" height="9" fill="#f37122"/><path d="M0 0l6 5 6-5" stroke="#121212" fill="none"/></svg>
      <span>info@vantrex.example</span></div>
  </div>

  <h5 style="left:881px;top:37px">Location Map</h5>
  <div class="abs map" role="img" aria-label="Street map showing the office location"></div>
</footer>

<!-- Copyright -->
<div class="abs copy">
  <p>Copyrights © 2016 All Rights Reserved by Vantrex Project Management Consulting</p>
  <span class="social" style="left:963px"></span>
  <span class="social" style="left:999px"></span>
  <span class="social" style="left:1035px"></span>
  <span class="social" style="left:1071px"></span>
</div>

</body>
</html>
```